Website Landing Page for Medical Recruitment

Looking for a landing page to add to our existing website. The objective of the page is to recruit new clinical staff for various departments within Larkfield Medical Center (non-profit hospital in the Richmond, TX area).

We would like the page to be modern, professional, and non-cluttered. Please include call-to-actions and include a button that will navigate to the page where candidates can submit their applications (this page already exists).

Target Market(s)

25-35-year-olds who live in the Houston and Richmond area with medical experience.

Industry/Entity Type

Medical/Health

Font styles to use
Sans Serif

Colors
0054AA
0677BA
7BADD7
CADEEF
E8F1F8

Requirements
Must have
• A "call to action"; a button that navigates to larkfieldmedhub.example/careers

```html
<!DOCTYPE html>
<html lang="en">
<head>
<meta charset="utf-8">
<title>Larkfield Medical Center – Careers</title>
<link href="https://fonts.googleapis.com/css2?family=Open+Sans:ital,wght@0,400;0,600;0,700;0,800;1,400&display=swap" rel="stylesheet">
<style>
:root{
  --navy:#0b3b67;
  --brand:#0054aa;
  --blue:#0677ba;
  --sky:#7badd7;
  --mist:#cadeef;
  --ice:#e8f1f8;
  --ink:#222;
  --muted:#777;
  --line:#e6e6e6;
  --foot:#272727;
  --foot-dark:#1b1b1b;
  --stage:#c9c9c9;
}
*{box-sizing:border-box;margin:0;padding:0}
html,body{width:1200px;height:3000px;overflow:hidden}
body{background:var(--stage);font-family:"Open Sans",sans-serif;color:var(--ink)}
a{text-decoration:none;color:inherit}
.page{position:absolute;left:0;top:0;width:1200px;height:2927px;background:#fff;overflow:hidden}
.abs{position:absolute}

/* top bar */
.topbar{left:0;top:0;width:1200px;height:54px;border-bottom:1px solid var(--line)}
.contact-line{left:162px;top:18px;font-size:12px;color:#666;display:flex;gap:22px;align-items:center}
.contact-line span{display:flex;align-items:center;gap:7px}
.social{right:162px;top:21px;display:flex;gap:12px}
.social i{display:block;width:9px;height:9px;border-radius:50%;background:var(--blue)}
.social i:last-child{background:#555}

/* header */
.header{left:0;top:54px;width:1200px;height:75px}
.brand{left:162px;top:22px;display:flex;align-items:center;gap:8px}
.brand-dot{width:22px;height:22px;border-radius:50%;background:var(--navy)}
.brand-name{font-size:17px;font-weight:600;color:var(--navy)}
.auth{right:162px;top:23px;display:flex;gap:5px}
.btn-login,.btn-signup{height:30px;padding:0 18px;font-size:12px;line-height:30px;color:#fff}
.btn-login{background:var(--navy)}
.btn-signup{background:#c8c8c8}

/* hero */
.hero{left:0;top:129px;width:1200px;height:449px;background:linear-gradient(100deg,#2a9fd9 0%,#1b86c6 40%,#1670ad 70%,#155a8d 100%)}
.hero-photo{position:absolute;inset:0;background:radial-gradient(ellipse at 28% 45%,rgba(10,60,110,.35),transparent 55%),radial-gradient(ellipse at 85% 70%,rgba(10,50,90,.3),transparent 50%)}
.hero-copy{position:absolute;left:0;right:0;top:140px;text-align:center;color:#fff}
.hero-copy h1{font-size:38px;font-weight:800;letter-spacing:1px}
.hero-copy p{font-size:14px;line-height:23px;margin-top:8px}
.btn-apply{display:inline-block;margin-top:20px;width:186px;height:48px;line-height:44px;border:2px solid #fff;border-radius:3px;font-size:15px;font-weight:700;color:#fff}

/* section titles */
.eyebrow{font-size:11px;color:#555;text-align:center;text-transform:uppercase}
.section-title{font-size:21px;font-weight:800;text-align:center;letter-spacing:.5px;color:#1a1a1a}
.section-title em{font-style:normal;color:var(--navy)}
.lede{font-size:10px;color:#666;text-align:center;line-height:19px}

/* process */
.process-head{left:0;top:656px;width:1200px}
.process-head .lede{width:500px;margin:6px auto 0}
.step{top:785px;width:277px;height:282px;text-align:center;border-bottom:2px solid var(--navy);padding-top:40px}
.step.active{background:var(--navy);color:#fff}
.step-icon{width:66px;height:66px;border-radius:50%;margin:0 auto;display:flex;align-items:center;justify-content:center}
.step h3{font-size:16px;font-weight:400;margin-top:22px}
.step p{font-size:10px;line-height:22px;margin:16px 30px 0;color:#777}
.step.active p{color:#dce7f2}

.divider{left:0;width:1200px;height:1px;background:var(--line)}

/* categories */
.tabs{left:162px;top:1212px;width:877px;border-bottom:2px solid var(--line);display:flex;gap:38px;font-size:11px;font-weight:600;color:#555}
.tabs span{padding-bottom:8px}
.tabs .on{color:var(--navy);border-bottom:2px solid var(--navy);margin-bottom:-2px}
.tiles{left:162px;top:1271px;display:flex;gap:22px}
.tile{width:128px;height:142px;position:relative}
.tile-label{position:absolute;left:0;right:0;bottom:12px;text-align:center;font-size:12px;font-weight:700;color:#fff}

/* jobs */
.jobs-head{left:0;top:1562px;width:1200px}
.jobs{left:162px;top:1668px;width:652px}
.job{height:75px;display:flex;align-items:center;font-size:10px;background:#f7f9fb}
.job:nth-child(even){background:#f2f6f9}
.job.hot{background:var(--navy);color:#fff}
.job-thumb{width:54px;height:54px;margin-left:12px;background:linear-gradient(135deg,#6d8aa4,#c9d6e0)}
.job-title{margin-left:10px;width:155px}
.job-title b{display:block;font-size:13px;font-weight:700}
.job-title small{font-size:9px;color:#666}
.job.hot .job-title small{color:#cfe0ef}
.job-dept{width:120px;color:#555}
.job.hot .job-dept{color:#fff;font-weight:600}
.job-addr{width:146px;display:flex;gap:5px;align-items:center;font-size:9px;line-height:11px;color:#555}
.job.hot .job-addr{color:#fff;font-weight:600}
.job-pay{width:53px;color:#555}
.job.hot .job-pay{color:#fff;font-weight:600}
.btn-job{width:77px;height:37px;line-height:37px;text-align:center;background:var(--navy);color:#fff;font-size:10px;font-weight:700;border-radius:2px}
.job.hot .btn-job{background:var(--blue)}
.more{left:162px;top:2061px;width:121px;height:34px;background:#e2e2e2;font-size:9px;color:#666;display:flex;align-items:center;justify-content:center;gap:7px}

.promo{left:837px;top:1668px;width:202px;height:374px;background:linear-gradient(180deg,#3a4750 0%,#243038 55%,#111 100%)}
.promo-bubble{position:absolute;left:100px;top:10px;width:104px;height:104px;border-radius:50%;background:#55c3f0;display:flex;align-items:center;justify-content:center}
.promo-bubble span{width:66px;height:52px;background:#fff;border-radius:26px;color:#55c3f0;font-size:36px;font-weight:800;text-align:center;line-height:52px}
.promo h4{position:absolute;left:14px;top:228px;color:#fff;font-size:26px;font-weight:800;line-height:33px;letter-spacing:-1.5px}
.promo a{position:absolute;left:12px;right:12px;top:320px;height:44px;line-height:44px;text-align:center;background:var(--blue);border:1px solid #fff;color:#fff;font-size:13px}

/* testimonials */
.quote-deco{left:0;top:2165px;width:281px;height:218px;background:linear-gradient(90deg,#ececec,#f3f3f3)}
.test-head{left:0;top:2238px;width:1200px}
.quote-card{left:311px;top:2325px;width:579px;height:104px;background:var(--navy);color:#fff;padding:20px 22px;font-size:11px;line-height:25px}
.quote-card cite{display:block;font-size:10px;font-weight:700;font-style:normal}
.quote-card cite i{font-weight:400}
.avatar{left:851px;top:2380px;width:60px;height:60px;border-radius:50%;border:3px solid #fff;background:linear-gradient(135deg,#d9c3b5,#8c6b5a)}
.dots{left:0;top:2453px;width:1200px;display:flex;justify-content:center;gap:6px}
.dots i{width:11px;height:11px;border-radius:50%;background:#ccc}
.dots i:first-child{background:var(--navy)}

/* footer */
.footer{left:0;top:2543px;width:1200px;height:330px;background:var(--foot);color:#aaa}
.foot-brand{left:162px;top:55px;display:flex;align-items:center;gap:8px}
.foot-brand .brand-dot{background:#fff}
.foot-brand .brand-name{color:#fff}
.foot-about{left:162px;top:123px;width:285px;font-size:11.5px;line-height:22.5px}
.foot-col h5{font-size:14px;font-weight:700;color:#fff;margin-bottom:32px}
.foot-col p{font-size:10px;line-height:18px}
.foot-col ul{list-style:none;font-size:10px;line-height:22.5px}
.bottombar{left:0;top:2873px;width:1200px;height:54px;background:var(--foot-dark);color:#fff;font-size:10px;padding:18px 162px}
</style>
</head>
<body>
<main class="page">

  <div class="abs topbar">
    <div class="abs contact-line">
      <span><svg width="12" height="12" viewBox="0 0 12 12"><path d="M2 1h3l1 3-2 1a6 6 0 0 0 3 3l1-2 3 1v3c-6 0-9-3-9-9z" fill="none" stroke="#666"/></svg>Call: 555-010-0142</span>
      <span><svg width="13" height="10" viewBox="0 0 13 10"><rect x=".5" y=".5" width="12" height="9" fill="none" stroke="#666"/><path d="M.5 .5l6 5 6-5" fill="none" stroke="#666"/></svg>jobs@larkfieldmed.example</span>
    </div>
    <div class="abs social" aria-label="Social links"><i></i><i></i><i></i><i></i></div>
  </div>

  <header class="abs header">
    <div class="abs brand"><span class="brand-dot"></span><span class="brand-name">Larkfield Medical Center</span></div>
    <nav class="abs auth"><a class="btn-login" href="#">Login</a><a class="btn-signup" href="#">Sign up</a></nav>
  </header>

  <section class="abs hero">
    <div class="hero-photo" role="img" aria-label="Blue-toned photo of nurses at work"></div>
    <div class="hero-copy">
      <h1>ARE YOU READY TO JOIN WITH US?</h1>
      <p>We're hiring for multiple nursing positions in a variety of our departments.<br>Join our team!</p>
      <a class="btn-apply" href="https://larkfieldmedhub.example/careers">APPLICATION NOW</a>
    </div>
  </section>

  <section>
    <div class="abs process-head">
      <div class="eyebrow">Our Process</div>
      <h2 class="section-title">HOW WE WORK FOR YOU?</h2>
      <p class="lede">Lorem ipsum dolor sit amet, consectetur adipisicing elit, sed do eiusmod tempor incididunt ut labore et dolore magna aliqua</p>
    </div>
    <div class="abs step" style="left:162px">
      <div class="step-icon" style="background:#e8493a"><span style="width:42px;height:42px;border-radius:50%;background:#fff;color:#e8493a;font-size:26px;font-weight:700;line-height:42px">?</span></div>
      <h3>Searching for the best job</h3>
      <p>Lorem Ipsum is simply dummy text of the printing and typesetting industry. Lorem Ipsum has been the industry's standard dummy text ever since the 1500s</p>
    </div>
    <div class="abs step active" style="left:462px">
      <div class="step-icon" style="background:#fff"><svg width="28" height="34" viewBox="0 0 28 34"><path d="M0 0h20l8 8v26H0z" fill="#6bbf4e"/><path d="M20 0v8h8z" fill="#4a9a33"/><rect x="6" y="18" width="16" height="3" fill="#fff"/></svg></div>
      <h3>Create Your Resume</h3>
      <p>Lorem Ipsum is simply dummy text of the printing and typesetting industry. Lorem Ipsum has been the industry's standard dummy text ever since the 1500s</p>
    </div>
    <div class="abs step" style="left:762px">
      <div class="step-icon" style="background:linear-gradient(180deg,#bfe3f5,#2c6f9a)" role="img" aria-label="Illustration of a nurse"></div>
      <h3>Face Interview Online</h3>
      <p>Lorem Ipsum is simply dummy text of the printing and typesetting industry. Lorem Ipsum has been the industry's standard dummy text ever since the 1500s</p>
    </div>
  </section>

  <div class="abs divider" style="top:1142px"></div>

  <section>
    <div class="abs tabs"><span class="on">Category</span><span>Employeers</span></div>
    <div class="abs tiles">
      <div class="tile" role="img" aria-label="Photo of a nurse" style="background:linear-gradient(180deg,#a87b62,#27466a)"><span class="tile-label">Nurse</span></div>
      <div class="tile" role="img" aria-label="Photo of a medical assistant" style="background:linear-gradient(180deg,#d9d2cc,#3c4c70)"></div>
      <div class="tile" role="img" aria-label="Photo of a radiology technician with a scanner" style="background:linear-gradient(180deg,#dfe6ec,#b8c4cf)"></div>
      <div class="tile" role="img" aria-label="Photo of a male nurse" style="background:linear-gradient(180deg,#e6e6e6,#1f3456)"></div>
      <div class="tile" role="img" aria-label="Photo of lab staff" style="background:linear-gradient(180deg,#9dbad0,#4c8cb8)"></div>
      <div class="tile" role="img" aria-label="Photo of a surgeon" style="background:linear-gradient(180deg,#b5d4ea,#5e90b8)"></div>
    </div>
  </section>

  <div class="abs divider" style="top:1489px"></div>

  <section>
    <div class="abs jobs-head">
      <div class="eyebrow">Recent Jobs</div>
      <h2 class="section-title"><em>54716</em> AVAILABLE JOBS FOR YOU</h2>
    </div>
    <div class="abs jobs">
      <div class="job"><div class="job-thumb" role="img" aria-label="Job photo"></div><div class="job-title"><b>Job Title here</b><small>Full Time</small></div><div class="job-dept">Lorem Ipsum</div><div class="job-addr"><svg width="7" height="10" viewBox="0 0 7 10"><path d="M3.5 0A3.5 3.5 0 0 0 0 3.5C0 6 3.5 10 3.5 10S7 6 7 3.5A3.5 3.5 0 0 0 3.5 0z" fill="#55c3f0"/></svg><span>1820 Harlow Street,<br>Alderton, Westland</span></div><div class="job-pay">14000$</div><a class="btn-job" href="#">Apply Now</a></div>
      <div class="job"><div class="job-thumb" role="img" aria-label="Job photo"></div><div class="job-title"><b>Job Title here</b><small>Full Time</small></div><div class="job-dept">Lorem Ipsum</div><div class="job-addr"><svg width="7" height="10" viewBox="0 0 7 10"><path d="M3.5 0A3.5 3.5 0 0 0 0 3.5C0 6 3.5 10 3.5 10S7 6 7 3.5A3.5 3.5 0 0 0 3.5 0z" fill="#55c3f0"/></svg><span>1820 Harlow Street,<br>Alderton, Westland</span></div><div class="job-pay">14000$</div><a class="btn-job" href="#">Apply Now</a></div>
      <div class="job"><div class="job-thumb" role="img" aria-label="Job photo"></div><div class="job-title"><b>Job Title here</b><small>Full Time</small></div><div class="job-dept">Lorem Ipsum</div><div class="job-addr"><svg width="7" height="10" viewBox="0 0 7 10"><path d="M3.5 0A3.5 3.5 0 0 0 0 3.5C0 6 3.5 10 3.5 10S7 6 7 3.5A3.5 3.5 0 0 0 3.5 0z" fill="#55c3f0"/></svg><span>1820 Harlow Street,<br>Alderton, Westland</span></div><div class="job-pay">35000$</div><a class="btn-job" href="#">Apply Now</a></div>
      <div class="job hot"><div class="job-thumb" role="img" aria-label="Job photo"></div><div class="job-title"><b>Job Title here</b><small>Part Time</small></div><div class="job-dept">Lorem Ipsum</div><div class="job-addr"><svg width="7" height="10" viewBox="0 0 7 10"><path d="M3.5 0A3.5 3.5 0 0 0 0 3.5C0 6 3.5 10 3.5 10S7 6 7 3.5A3.5 3.5 0 0 0 3.5 0z" fill="#55c3f0"/></svg><span>1820 Harlow Street,<br>Alderton, Westland</span></div><div class="job-pay">14000$</div><a class="btn-job" href="#">Apply Now</a></div>
      <div class="job"><div class="job-thumb" role="img" aria-label="Job photo"></div><div class="job-title"><b>Job Title here</b><small>Full Time</small></div><div class="job-dept">Lorem Ipsum</div><div class="job-addr"><svg width="7" height="10" viewBox="0 0 7 10"><path d="M3.5 0A3.5 3.5 0 0 0 0 3.5C0 6 3.5 10 3.5 10S7 6 7 3.5A3.5 3.5 0 0 0 3.5 0z" fill="#55c3f0"/></svg><span>1820 Harlow Street,<br>Alderton, Westland</span></div><div class="job-pay">154000$</div><a class="btn-job" href="#">Apply Now</a></div>
    </div>
    <a class="abs more" href="#"><svg width="11" height="11" viewBox="0 0 11 11"><path d="M9.5 5.5A4 4 0 1 1 8 2.3M8 0v2.5H5.5" fill="none" stroke="#666"/></svg>View More Jobs</a>

    <aside class="abs promo" role="img" aria-label="Photo of a nurse in green scrubs">
      <div class="promo-bubble"><span>?</span></div>
      <h4>SEEKING A<br>JOB?</h4>
      <a href="https://larkfieldmedhub.example/careers">Create a Account</a>
    </aside>
  </section>

  <div class="abs divider" style="top:2165px"></div>

  <section>
    <div class="abs quote-deco" role="img" aria-label="Large faint quotation marks"></div>
    <div class="abs test-head">
      <div class="eyebrow">Testimonials</div>
      <h2 class="section-title">WHAT PEOPLES ARE SAYING</h2>
    </div>
    <blockquote class="abs quote-card">
      Lorem Ipsum is simply dummy text of the printing and typesetting industry. Lorem Ipsum has<br>been the industry's standard dummy text ever since the 1500s
      <cite>Marisol, <i>Medical Student</i></cite>
    </blockquote>
    <div class="abs avatar" role="img" aria-label="Portrait of the reviewer"></div>
    <div class="abs dots"><i></i><i></i><i></i><i></i></div>
  </section>

  <footer class="abs footer">
    <div class="abs foot-brand"><span class="brand-dot"></span><span class="brand-name">Larkfield Medical Center</span></div>
    <p class="abs foot-about">Larkfield Medical Center is passionately focused on patient-centered medicine. We have up-ended the traditional nursing model, putting the patient in the driver's seat when it comes to his or her plan of care. We believe – and research shows – that your communication and cooperation have more to do with your outcome than anything we do.</p>
    <div class="abs foot-col" style="left:562px;top:52px">
      <h5>Contact Us</h5>
      <p>Tel: 555-010-0142</p>
      <p style="margin-top:5px">Email: info@larkfieldmed.example, jobs@larkfieldmed.example</p>
      <p style="margin-top:5px;line-height:16px">Location: Larkfield Medical Center<br>Harlow Street Hospital Campus<br>1820 Harlow Street, Alderton<br>Westland 00142</p>
    </div>
    <div class="abs foot-col" style="left:919px;top:52px">
      <h5>Useful lnks</h5>
      <ul><li>Home</li><li>Find A Doctor</li><li>COVID-19</li><li>About Us</li><li>Services</li><li>Locations</li><li>Patients/Visitors</li><li>Ways To Give</li><li>Health Library</li></ul>
    </div>
  </footer>
  <div class="abs bottombar">(C) Larkfield2022, All rights reserved</div>
</main>
</body>
</html>
```